Postcard Design

Bramble Circuit Holdings is a waste and Recycling company. We want to purchase recyclable materials from businesses. We would like to use the colors green and grey. The exact colors needed in this project are described below. We would like to have a picture of waste cardboard,a picture of money, and and the line- Are you getting top dollar for your Recyclables? After please put our logo and our phone number: 800.472.5196, our website (tindlepath.com),
and our email address: marguerite@tindlepath.com.

* Postcard must contain our logo. Please see buisness card for branding

Industry/Entity Type

It Company

Requirements
Must have
• This postcard must contain the logo and these colors:
Pantone: 576C & 418C

```html
<!DOCTYPE html>
<html lang="en">
<head>
<meta charset="utf-8">
<title>Bramble Circuit Holdings Postcard</title>
<link rel="stylesheet" href="https://fonts.googleapis.com/css2?family=Roboto:wght@300;700&family=Roboto+Condensed:wght@400;700&display=swap">
<style>
  :root {
    --stage: #4d4d50;
    --brand-green: #5b8a3a;
    --brand-grey: #5d5e4c;
    --ink: #1d1d1d;
    --paper: #ffffff;
    --field-edge: #dfe1de;
    --field-centre: #fbfbfa;
    --accent-yellow: #f2e600;
    --cardboard-light: #d6a877;
    --cardboard-dark: #b9875a;
    --money-light: #e3e6d6;
    --money-dark: #a9b39a;
  }
  * { box-sizing: border-box; margin: 0; padding: 0; }
  html, body {
    width: 958px; height: 1200px; overflow: hidden;
    background: var(--stage);
  }
  .postcard {
    position: absolute; left: 76px; top: 78px;
    width: 804px; height: 1045px;
    background: var(--paper);
    overflow: hidden;
  }
  .hero {
    position: absolute; left: 0; top: 0; width: 804px; height: 838px;
    background: radial-gradient(ellipse at 50% 45%, var(--field-centre) 0%, #f1f2f0 55%, var(--field-edge) 100%);
  }
  .photo-cardboard {
    position: absolute; left: 117px; top: 37px; width: 610px; height: 255px;
    background: linear-gradient(160deg, var(--cardboard-light), var(--cardboard-dark));
    border-radius: 4px;
  }
  .flow-arrow {
    position: absolute; left: 360px; top: 312px; width: 86px; height: 96px;
  }
  .photo-money {
    position: absolute; left: 152px; top: 432px; width: 500px; height: 235px;
    background: linear-gradient(170deg, var(--money-light), var(--money-dark));
    border-radius: 3px;
  }
  .headline {
    position: absolute; left: 0; top: 705px; width: 804px;
    text-align: center;
    font-family: "Roboto", Arial, sans-serif;
    font-weight: 300; font-size: 41px; line-height: 52px;
    color: var(--ink); letter-spacing: 0.2px;
  }
  .headline strong { font-weight: 700; }
  .contact-band {
    position: absolute; left: 0; top: 838px; width: 804px; height: 46px;
    background: var(--brand-green);
    display: flex; align-items: center; justify-content: center; gap: 18px;
    font-family: "Roboto Condensed", Arial, sans-serif;
    font-weight: 700; font-size: 22px; color: var(--paper);
  }
  .contact-item { display: flex; align-items: center; gap: 6px; }
  .contact-item svg { width: 22px; height: 16px; }
  .footer {
    position: absolute; left: 0; top: 884px; width: 804px; height: 161px;
    background: var(--paper);
  }
  .contact-label {
    position: absolute; left: 42px; top: 55px;
    font-family: "Roboto Condensed", Arial, sans-serif;
    font-size: 18px; color: var(--ink);
  }
  .contact-name {
    position: absolute; left: 40px; top: 80px;
    font-family: "Roboto Condensed", Arial, sans-serif;
    font-weight: 700; font-size: 25px; color: var(--brand-green);
    letter-spacing: 0.3px;
  }
  .brand {
    position: absolute; right: 52px; top: 56px;
    display: flex; align-items: center; gap: 10px;
  }
  .brand-square { width: 22px; height: 22px; background: var(--brand-grey); }
  .brand-name {
    font-family: "Roboto Condensed", Arial, sans-serif;
    font-weight: 700; font-size: 25px; color: var(--brand-green);
  }
</style>
</head>
<body>
  <main class="postcard">
    <section class="hero">
      <div class="photo-cardboard" role="img" aria-label="Photo of flattened waste cardboard boxes stacked together"></div>
      <svg class="flow-arrow" viewBox="0 0 86 96" aria-hidden="true">
        <polygon points="0,0 43,26 86,0 86,28 43,54 0,28" fill="var(--brand-green)"/>
        <polygon points="0,42 43,68 86,42 86,70 43,96 0,70" fill="var(--brand-grey)"/>
      </svg>
      <div class="photo-money" role="img" aria-label="Photo of a stack of hundred dollar banknotes"></div>
      <h1 class="headline">ARE YOU GETTING <strong>TOP DOLLAR</strong><br>FOR YOUR <strong>RECYCLABLES?</strong></h1>
    </section>

    <div class="contact-band">
      <span class="contact-item">
        <svg viewBox="0 0 22 16" aria-hidden="true"><polygon points="0,0 5,0 11,8 5,16 0,16 6,8" fill="var(--accent-yellow)"/><polygon points="10,0 15,0 21,8 15,16 10,16 16,8" fill="var(--accent-yellow)"/></svg>
        800.472.5196
      </span>
      <span class="contact-item">
        <svg viewBox="0 0 22 16" aria-hidden="true"><polygon points="0,0 5,0 11,8 5,16 0,16 6,8" fill="var(--accent-yellow)"/><polygon points="10,0 15,0 21,8 15,16 10,16 16,8" fill="var(--accent-yellow)"/></svg>
        marguerite@tindlepath.com.
      </span>
      <span class="contact-item">
        <svg viewBox="0 0 22 16" aria-hidden="true"><polygon points="0,0 5,0 11,8 5,16 0,16 6,8" fill="var(--accent-yellow)"/><polygon points="10,0 15,0 21,8 15,16 10,16 16,8" fill="var(--accent-yellow)"/></svg>
        www.tindlepath.com
      </span>
    </div>

    <footer class="footer">
      <p class="contact-label">For More Contact :</p>
      <p class="contact-name">MARGUERITE VANTREEL</p>
      <div class="brand">
        <span class="brand-square" aria-hidden="true"></span>
        <span class="brand-name">Bramble Circuit Holdings</span>
      </div>
    </footer>
  </main>
</body>
</html>
```